Kitchen Tools Infographic - Helpful Items for Healthy Home Meals

We are a weight loss company that provides holistic, natural nutrition programs to consumers -- you can see our web site at www.FernaluVita.com. We need a simple infographic to be shared on social media and via email. The topic for the infographic is "Equip Your Kitchen for Healthy Home Meals". We've outlined 5 groups of kitchen tools that are helpful for consumers to have for preparing home meals, and included some framing statistics emphasizing the weight management benefits of preparing meals versus eating out.

Target Market(s)

Women age 35-55

Industry/Entity Type

Health And Wellness

Font styles to use
Sans Serif

Colors
0292cd
9bcb3b

Requirements
Must have
• - FernaluVita Logo
• - Graphics summarizing statistic (weight gain)
• - Graphics showing groupings of kitchen tools
Should not have
• body scale graphics
• before/after graphics

```html
<!DOCTYPE html>
<html lang="en">
<head>
<meta charset="utf-8">
<title>Equip Your Kitchen for Healthy Home Meals – FernaluVita</title>
<link rel="stylesheet" href="https://fonts.googleapis.com/css2?family=Open+Sans:wght@400;600;700&family=Oswald:wght@300;400&display=swap">
<style>
  :root{
    --blue:#0292cd;
    --cyan:#00b3d1;
    --green:#9bcb3b;
    --green-dark:#8cbf2e;
    --ink:#555b61;
    --muted:#8a8f94;
    --grid:#e4e6e8;
    --panel:#efeff0;
    --card-line:#dcdcdc;
    --footer:#333536;
    --white:#ffffff;
  }
  *{box-sizing:border-box;margin:0;padding:0}
  html,body{width:1200px;height:3214px;overflow:hidden;background:var(--white)}
  body{position:relative;font-family:"Open Sans",Arial,sans-serif;color:var(--ink)}

  /* Hero */
  .hero{position:absolute;left:0;top:0;width:1200px;height:364px;
    background:linear-gradient(90deg,#3a3b3a 0%,#6d6a62 35%,#8b8478 55%,#5b4d3e 80%,#3f3a33 100%)}
  .hero-photo{position:absolute;inset:0}
  .hero-title{position:absolute;left:0;width:100%;text-align:center;font-weight:600;letter-spacing:3px}
  .hero-title.main{top:62px;font-size:88px;color:var(--cyan)}
  .hero-title.sub{top:198px;font-size:66px;color:var(--green)}

  /* Why section */
  .why{position:absolute;left:0;top:364px;width:1200px;height:890px;background:var(--white)}
  .section-heading{position:absolute;left:0;width:100%;text-align:center;font-size:42px;font-weight:600;color:var(--blue)}
  .why .section-heading{top:64px}
  .why-copy{position:absolute;left:110px;width:980px;top:160px;text-align:center;font-size:27px;line-height:44px;color:var(--muted)}
  .chart-title{position:absolute;text-align:center;font-size:28px;line-height:44px;color:var(--blue)}
  .chart{position:absolute}

  /* Tools section */
  .tools{position:absolute;left:0;top:1254px;width:1200px;height:1371px;background:var(--panel)}
  .tools .section-heading{top:50px}
  .tool-column{position:absolute;top:154px;width:195px;height:1179px;background:var(--white);border:2px solid var(--card-line)}
  .step-number{position:absolute;top:20px;width:100%;text-align:center;font-family:"Oswald",Arial,sans-serif;font-weight:300;font-size:60px;line-height:80px}
  .step-band{position:absolute;left:-2px;top:90px;width:195px;height:232px}
  .step-label{position:absolute;left:0;top:136px;width:100%;text-align:center;font-family:"Oswald",Arial,sans-serif;font-weight:300;font-size:62px;color:var(--white)}
  .tool-item{position:absolute;left:0;width:100%;text-align:center}
  .tool-icon{display:block;margin:0 auto;width:96px;height:96px;border-radius:10px}
  .tool-name{margin-top:20px;font-family:"Oswald",Arial,sans-serif;font-weight:400;font-size:17px;text-transform:uppercase;letter-spacing:.3px}
  .tool-note{margin:8px auto 0;width:170px;font-size:15.5px;line-height:21px;color:var(--muted)}
  .is-blue .step-number,.is-blue .tool-name{color:var(--cyan)}
  .is-green .step-number,.is-green .tool-name{color:var(--green)}
  .is-blue .tool-icon{background:#dff2f7}
  .is-green .tool-icon{background:#eef6df}

  /* Footer */
  .cta{position:absolute;left:0;top:2625px;width:1200px;height:493px;background:var(--footer);text-align:center}
  .cta-line{position:absolute;left:0;top:52px;width:100%;font-size:34px;color:var(--white)}
  .cta-line .brand{color:var(--cyan);font-weight:700}
  .cta-invite{position:absolute;left:0;top:148px;width:100%;font-size:27px;font-weight:600;color:var(--green)}
  .cta-button{position:absolute;left:529px;top:221px;width:167px;height:62px;background:var(--green);border-radius:3px;
    font-size:20px;font-weight:700;color:var(--white);line-height:62px}
  .brand-mark{position:absolute;left:0;top:330px;width:100%;display:flex;justify-content:center;align-items:center;gap:22px}
  .brand-dot{width:60px;height:60px;border-radius:50%;background:var(--green)}
  .brand-name{font-size:44px;font-weight:700;color:var(--white)}
  .cta-url{position:absolute;left:0;top:410px;width:100%;font-size:37px;color:var(--cyan)}

  .sources{position:absolute;left:26px;top:3130px;font-size:14px;line-height:28px;color:var(--muted)}
  .sources span{display:block;padding-left:62px}
  .sources span:first-child{padding-left:0}
</style>
</head>
<body>

<header class="hero">
  <div class="hero-photo" role="img" aria-label="Kitchen counter with fresh vegetables and cooking ingredients"></div>
  <h1 class="hero-title main">EQUIP YOUR KITCHEN</h1>
  <p class="hero-title sub">FOR HEALTHY HOME MEALS</p>
</header>

<section class="why">
  <h2 class="section-heading">Why Cook at Home?</h2>
  <p class="why-copy">Those who eat out consume an average of 134 calories more per meal.&nbsp; Americans eat out an average of 4.5 times per week, so those extra calories can add up to substantial weight gain -- and give you a reason to prepare your own meals.</p>

  <div class="chart-title" style="left:171px;top:346px;width:390px">Excess Calories From<br>Restaurant Meals</div>
  <svg class="chart" style="left:150px;top:461px" width="380" height="380" viewBox="0 0 380 380" font-family="Open Sans, Arial, sans-serif">
    <g stroke="#e4e6e8" stroke-width="2">
      <line x1="62" y1="24" x2="370" y2="24"/><line x1="62" y1="75" x2="370" y2="75"/>
      <line x1="62" y1="127" x2="370" y2="127"/><line x1="62" y1="178" x2="370" y2="178"/>
      <line x1="62" y1="230" x2="370" y2="230"/><line x1="62" y1="281" x2="370" y2="281"/>
    </g>
    <g fill="#8a8f94" font-size="16" text-anchor="end">
      <text x="56" y="29">600</text><text x="56" y="80">500</text><text x="56" y="132">400</text>
      <text x="56" y="183">300</text><text x="56" y="235">200</text><text x="56" y="286">100</text>
    </g>
    <line x1="62" y1="24" x2="62" y2="333" stroke="#c8cbce" stroke-width="2"/>
    <line x1="62" y1="333" x2="370" y2="333" stroke="#c8cbce" stroke-width="2"/>
    <rect x="125" y="264" width="28" height="69" fill="#9bcb3b"/>
    <rect x="230" y="23" width="28" height="310" fill="#9bcb3b"/>
    <g fill="#8a8f94" font-size="15" text-anchor="middle">
      <text x="139" y="356">Calories per</text><text x="139" y="374">Meal</text>
      <text x="244" y="356">Calories per</text><text x="244" y="374">Week</text>
    </g>
  </svg>

  <div class="chart-title" style="left:660px;top:346px;width:390px">Pounds Gained From<br>Restaurant Meals</div>
  <svg class="chart" style="left:660px;top:461px" width="380" height="380" viewBox="0 0 380 380" font-family="Open Sans, Arial, sans-serif">
    <g stroke="#e4e6e8" stroke-width="2">
      <line x1="50" y1="24" x2="360" y2="24"/><line x1="50" y1="75" x2="360" y2="75"/>
      <line x1="50" y1="127" x2="360" y2="127"/><line x1="50" y1="178" x2="360" y2="178"/>
      <line x1="50" y1="230" x2="360" y2="230"/><line x1="50" y1="281" x2="360" y2="281"/>
    </g>
    <g fill="#8a8f94" font-size="16" text-anchor="end">
      <text x="42" y="29">12</text><text x="42" y="80">10</text><text x="42" y="132">8</text>
      <text x="42" y="183">6</text><text x="42" y="235">4</text><text x="42" y="286">2</text>
    </g>
    <line x1="50" y1="24" x2="50" y2="333" stroke="#c8cbce" stroke-width="2"/>
    <line x1="50" y1="333" x2="360" y2="333" stroke="#c8cbce" stroke-width="2"/>
    <rect x="92" y="256" width="28" height="77" fill="#9bcb3b"/>
    <rect x="192" y="214" width="28" height="119" fill="#9bcb3b"/>
    <rect x="292" y="101" width="28" height="232" fill="#9bcb3b"/>
    <g fill="#8a8f94" font-size="15" text-anchor="middle">
      <text x="106" y="360">2 months</text><text x="206" y="360">6 months</text><text x="306" y="360">1 year</text>
    </g>
  </svg>
</section>

<section class="tools">
  <h2 class="section-heading">Make Healthy Eating Easier With These Kitchen Tools</h2>

  <article class="tool-column is-blue" style="left:71px">
    <div class="step-number">01</div>
    <svg class="step-band" viewBox="0 0 195 232" preserveAspectRatio="none"><polygon points="0,0 97.5,50 195,0 195,232 0,232" fill="#00b3d1"/></svg>
    <div class="step-label">PREP</div>
    <div class="tool-item" style="top:356px"><span class="tool-icon" role="img" aria-label="Cutting board icon"></span><div class="tool-name">Cutting Board</div><p class="tool-note">essential for prepping meat and vegetables</p></div>
    <div class="tool-item" style="top:620px"><span class="tool-icon" role="img" aria-label="Chef's knife icon"></span><div class="tool-name">Chef's Knife</div><p class="tool-note">go for quality to make chopping, dicing and slicing faster and easier</p></div>
    <div class="tool-item" style="top:880px"><span class="tool-icon" role="img" aria-label="Digital food scale icon"></span><div class="tool-name">Digital Food Scale</div><p class="tool-note">get the precision you need for perfect recipes and portion control</p></div>
  </article>

  <article class="tool-column is-green" style="left:285px">
    <div class="step-number">02</div>
    <svg class="step-band" viewBox="0 0 195 232" preserveAspectRatio="none"><polygon points="0,0 97.5,50 195,0 195,232 0,232" fill="#9bcb3b"/></svg>
    <div class="step-label">TECH</div>
    <div class="tool-item" style="top:356px"><span class="tool-icon" role="img" aria-label="High-powered blender icon"></span><div class="tool-name">High-Powered Blender</div><p class="tool-note">make highly nutritious, healthy drinks from fruits and veggies</p></div>
    <div class="tool-item" style="top:620px"><span class="tool-icon" role="img" aria-label="Slow cooker icon"></span><div class="tool-name">Slow Cooker</div><p class="tool-note">cook delicious meals while you are at work</p></div>
    <div class="tool-item" style="top:880px"><span class="tool-icon" role="img" aria-label="Pressure cooker icon"></span><div class="tool-name">Pressure Cooker</div><p class="tool-note">create single pot meals in 20 minutes or less</p></div>
  </article>

  <article class="tool-column is-blue" style="left:501px">
    <div class="step-number">03</div>
    <svg class="step-band" viewBox="0 0 195 232" preserveAspectRatio="none"><polygon points="0,0 97.5,50 195,0 195,232 0,232" fill="#00b3d1"/></svg>
    <div class="step-label">COOK</div>
    <div class="tool-item" style="top:356px"><span class="tool-icon" role="img" aria-label="Ceramic pan icon"></span><div class="tool-name">Ceramic Pan</div><p class="tool-note">nonstick cooking surface allows you to cook without oil</p></div>
    <div class="tool-item" style="top:620px"><span class="tool-icon" role="img" aria-label="Vegetable steamer icon"></span><div class="tool-name">Vegetable Steamer</div><p class="tool-note">preserve nutrients and natural, fresh taste</p></div>
    <div class="tool-item" style="top:880px"><span class="tool-icon" role="img" aria-label="Baking sheet icon"></span><div class="tool-name">Baking Sheet</div><p class="tool-note">ideal for roasting vegetables in the oven or baking chicken and fish dishes</p></div>
  </article>

  <article class="tool-column is-green" style="left:718px">
    <div class="step-number">04</div>
    <svg class="step-band" viewBox="0 0 195 232" preserveAspectRatio="none"><polygon points="0,0 97.5,50 195,0 195,232 0,232" fill="#9bcb3b"/></svg>
    <div class="step-label">SERVE</div>
    <div class="tool-item" style="top:356px"><span class="tool-icon" role="img" aria-label="Cloth napkins icon"></span><div class="tool-name">Cloth Napkins</div><p class="tool-note">to reduce waste and dress up your table</p></div>
    <div class="tool-item" style="top:620px"><span class="tool-icon" role="img" aria-label="Dinnerware icon"></span><div class="tool-name">Dinnerware</div><p class="tool-note">pre-plate meals rather than serving family style to control portions</p></div>
    <div class="tool-item" style="top:880px"><span class="tool-icon" role="img" aria-label="Small plates icon"></span><div class="tool-name">Small Plates</div><p class="tool-note">use salad plates and smaller dishware to manage perception of food volume</p></div>
  </article>

  <article class="tool-column is-blue" style="left:936px">
    <div class="step-number">05</div>
    <svg class="step-band" viewBox="0 0 195 232" preserveAspectRatio="none"><polygon points="0,0 97.5,50 195,0 195,232 0,232" fill="#00b3d1"/></svg>
    <div class="step-label">STORE</div>
    <div class="tool-item" style="top:356px"><span class="tool-icon" role="img" aria-label="Glass storage containers icon"></span><div class="tool-name">Glass Storage Containers</div><p class="tool-note">keep your healthy left-overs so nothing goes to waste</p></div>
    <div class="tool-item" style="top:620px"><span class="tool-icon" role="img" aria-label="Mason jar icon"></span><div class="tool-name">Mason Jars</div><p class="tool-note">perfect for premade salads that you can bring to work</p></div>
    <div class="tool-item" style="top:880px"><span class="tool-icon" role="img" aria-label="Freezer bag icon"></span><div class="tool-name">Freezer Safe Re-Sealable Bags</div><p class="tool-note">prepare double batches to make the most of your time</p></div>
  </article>
</section>

<footer class="cta">
  <p class="cta-line"><span class="brand">FernaluVita</span> &nbsp;can help you develop healthier eating habits</p>
  <p class="cta-invite">We invite you to learn more.</p>
  <div class="cta-button">CONTACT US</div>
  <div class="brand-mark"><span class="brand-dot"></span><span class="brand-name">FernaluVita</span></div>
  <p class="cta-url">www.FernaluVita.com</p>
</footer>

<div class="sources">
  <span>Sources:&nbsp; https://www.foodstatsreview.org/2010/june/eating-out-increases-daily-calorie-intake/</span>
  <span>https://www.diningsurveyhub.com/b/the-state-of-american-dining-in-2016</span>
</div>

</body>
</html>
```